New business card for civil engineering company - "Keystone Audit"

We need a business card designed for our new structural engineering company.

The company name is "Keystone Audit" logo files attached.

We would like the following:
* Two-sided card
* Simple design

Information to be placed on the card:
Name - Marcus Dellow
Job Title - Director / Structural Engineer
Credentials - BEng(Hons), CPEng, CMengNZ, IntPE(NZ)
Email - marcus.dellow@keystoneaudit.co.nz
mobile - 0219364058
website - www.keystoneaudit.co.nz

```html
<!DOCTYPE html>
<html lang="en">
<head>
<meta charset="utf-8">
<title>Keystone Audit — Business Card</title>
<link href="https://fonts.googleapis.com/css2?family=Open+Sans:wght@400;600;700&display=swap" rel="stylesheet">
<style>
  :root {
    --stage: #2a2d31;
    --navy: #0f5387;
    --navy-deep: #0b4672;
    --blue-mid: #3a8fd0;
    --blue-light: #a9d9f0;
    --paper: #ffffff;
    --ink: #2b2b2b;
    --ink-soft: #6b6b6b;
    --rule: #8a8f96;
  }
  * { box-sizing: border-box; margin: 0; padding: 0; }
  html, body {
    width: 1200px; height: 900px; overflow: hidden;
    background: var(--stage);
    font-family: "Open Sans", sans-serif;
  }
  .stage {
    position: relative; width: 1200px; height: 900px;
    display: flex; align-items: center; justify-content: center; gap: 60px;
  }
  .card {
    position: relative; width: 520px; height: 318px; overflow: hidden;
    border-radius: 3px;
    box-shadow: 0 12px 30px rgba(0,0,0,.45);
  }

  /* Front */
  .card-front { background: var(--paper); }
  .front-strip {
    position: absolute; left: 0; top: 0; bottom: 0; width: 22px;
    background: var(--navy);
  }
  .front-rule {
    position: absolute; left: 28px; top: 0; bottom: 0; width: 2px;
    background: var(--rule);
  }
  .front-details { position: absolute; left: 58px; top: 34px; color: var(--ink-soft); }
  .person-name {
    font-size: 27px; color: var(--ink); letter-spacing: .5px; line-height: 1.1;
    text-transform: uppercase;
  }
  .person-name .first { font-weight: 700; }
  .person-name .last { font-weight: 400; }
  .person-role, .person-credentials { font-size: 13px; line-height: 1.35; }
  .person-role { margin-top: 4px; }
  .contact-list { list-style: none; margin-top: 10px; }
  .contact-list li {
    display: flex; align-items: center; gap: 10px;
    font-size: 13.5px; line-height: 1.55; color: #4a4a4a;
  }
  .contact-list svg { width: 13px; height: 13px; flex: none; }
  .front-accent {
    position: absolute; right: 0; bottom: 0; width: 300px; height: 150px;
    background: linear-gradient(160deg, rgba(169,217,240,.0) 0%, var(--blue-light) 35%, var(--blue-mid) 100%);
  }

  /* Back */
  .card-back {
    background: linear-gradient(135deg, var(--navy) 0%, var(--navy-deep) 100%);
    display: flex; flex-direction: column; align-items: center; justify-content: center;
    color: var(--paper);
  }
  .brand-mark { display: flex; align-items: center; gap: 10px; }
  .brand-square { width: 14px; height: 14px; background: var(--paper); }
  .brand-name {
    font-size: 30px; font-weight: 600; letter-spacing: 2px; text-transform: uppercase;
  }
  .brand-tagline {
    margin-top: 6px; font-size: 11px; letter-spacing: 3.2px; text-transform: uppercase;
    font-weight: 400;
  }
</style>
</head>
<body>
<main class="stage">
  <section class="card card-front" aria-label="Card front">
    <div class="front-strip"></div>
    <div class="front-rule"></div>
    <div class="front-details">
      <h1 class="person-name"><span class="first">Marcus</span> <span class="last">Dellow</span></h1>
      <p class="person-role">Director / Structural Engineer</p>
      <p class="person-credentials">BEng(Hons), CPEng, CMengNZ, IntPE(NZ)</p>
      <ul class="contact-list">
        <li>
          <svg viewBox="0 0 16 16" aria-hidden="true"><path fill="#0f5387" d="M4 1.5l2.2 2.6-1.3 1.6c.8 1.9 2.2 3.3 4.1 4.1l1.6-1.3 2.6 2.2-1.2 2.4C7 13 3 9 2.9 2.7z"/></svg>
          021 936 4058
        </li>
        <li>
          <svg viewBox="0 0 16 16" aria-hidden="true"><rect x="1" y="3" width="14" height="10" fill="#0f5387"/><path d="M1 3l7 5 7-5" fill="none" stroke="#fff" stroke-width="1.2"/></svg>
          marcus.dellow@keystoneaudit.co.nz
        </li>
        <li>
          <svg viewBox="0 0 16 16" aria-hidden="true"><circle cx="8" cy="8" r="7" fill="#0f5387"/><path d="M1 8h14M8 1c-3 3.5-3 10.5 0 14M8 1c3 3.5 3 10.5 0 14" fill="none" stroke="#fff" stroke-width=".9"/></svg>
          www.keystoneaudit.co.nz
        </li>
      </ul>
    </div>
    <div class="front-accent" role="img" aria-label="Angular blue decorative graphic"></div>
  </section>

  <section class="card card-back" aria-label="Card back">
    <div class="brand-mark">
      <span class="brand-square"></span>
      <span class="brand-name">Keystone Audit</span>
    </div>
    <p class="brand-tagline">Peer Review Specialists</p>
  </section>
</main>
</body>
</html>
```